Varga Lillas Physiotherapy Business Card Vienna

We need a business card design for a newly created Physiotherapy company based in Vienna Austria.
We seek a simple, modern, minimalist design without too much color variation. The font should look young/fresh, but definitely not childish or so. Since we are a starting Business, we currently haven't got a logo, if you feel like a logo would fit your design, feel free to use one, but it's not necessary.
Target Market(s)
Healthcare, young and elderly people with mobility issues
Industry/Entity Type
Health And Wellness
Contact Information for Business Card
Name: Lilla Varga
Title description: Physiotherapist
Phone num: +43 664 5290 4816
e-mail: lilla.praxis@brelomail.com
Colors
Designer to choose colors to be used in the design.
Requirements
Must have
- Final design language must be in German, basically, the Title Description needs to be "Physiotherapeutin" the other details remain as in the English Language.
Nice to have
- Simple, modern, minimalist design
Should not have
- too many colors, Obvious use of a skeleton, skull, spline

```html
<!DOCTYPE html>
<html lang="de">
<head>
<meta charset="utf-8">
<title>Varga Lillas Physiotherapy – Visitenkarte</title>
<link href="https://fonts.googleapis.com/css2?family=Montserrat:wght@300;400&display=swap" rel="stylesheet">
<style>
  :root {
    --stage: #1c1c1c;
    --accent: #e05427;
    --paper: #ffffff;
    --ink: #111111;
    --on-accent: #ffffff;
  }
  * { margin: 0; padding: 0; box-sizing: border-box; }
  html, body {
    width: 1200px;
    height: 1200px;
    overflow: hidden;
    background: var(--stage);
    font-family: "Montserrat", sans-serif;
  }
  .canvas {
    position: relative;
    width: 1200px;
    height: 1200px;
  }
  .card {
    position: absolute;
    left: 210px;
    width: 780px;
    height: 480px;
    border-radius: 24px;
  }
  .card--front {
    top: 90px;
    background: var(--accent);
    color: var(--on-accent);
    display: flex;
    align-items: center;
    justify-content: center;
  }
  .brand {
    text-align: left;
    margin-left: 60px;
  }
  .brand__name {
    font-weight: 400;
    font-size: 34px;
    letter-spacing: 0.2em;
    line-height: 1;
  }
  .brand__field {
    font-weight: 300;
    font-size: 15px;
    letter-spacing: 0.72em;
    margin-top: 8px;
    margin-left: -6px;
  }
  .card--back {
    top: 630px;
    background: var(--paper);
    color: var(--ink);
    padding: 70px 0 0 96px;
  }
  .wordmark {
    display: flex;
    align-items: center;
    gap: 12px;
    font-weight: 300;
    font-size: 22px;
    letter-spacing: 0.25em;
    height: 90px;
  }
  .wordmark__dot {
    width: 14px;
    height: 14px;
    border-radius: 50%;
    background: var(--ink);
  }
  .person__name {
    margin-top: 26px;
    font-weight: 400;
    font-size: 42px;
    letter-spacing: 0.24em;
    line-height: 1;
  }
  .person__title {
    margin-top: 10px;
    font-weight: 300;
    font-size: 18px;
    letter-spacing: 0.16em;
  }
  .divider {
    width: 22px;
    height: 2px;
    background: var(--ink);
    margin: 12px 0 18px;
  }
  .contact {
    list-style: none;
    font-weight: 400;
    font-size: 19px;
    letter-spacing: 0.14em;
    line-height: 1.5;
  }
</style>
</head>
<body>
  <main class="canvas">
    <section class="card card--front">
      <div class="brand">
        <div class="brand__name">VARGA LILLAS</div>
        <div class="brand__field">PHYSIOTHERAPY</div>
      </div>
    </section>

    <section class="card card--back">
      <div class="wordmark">
        <span class="wordmark__dot"></span>
        <span>VARGA LILLAS</span>
      </div>
      <h1 class="person__name">LILLA VARGA</h1>
      <p class="person__title">PHYSIOTHERAPEUTIN</p>
      <div class="divider"></div>
      <ul class="contact">
        <li class="contact__phone">+43 664 5290 4816</li>
        <li class="contact__email">lilla.praxis@brelomail.com</li>
      </ul>
    </section>
  </main>
</body>
</html>
```